Copperfield Roofing Co. business card design

I am a Roofing contractor in Texas. The name of my company is Copperfield Roofing Co. I also offer a few other services (Christmas light installation, gutters, fencing, pressure washing). However my main gig is roofing. Storm restoration and knowledge of the insurance claim process is my specialty.

My colors are black, red and white. I’d like something pretty simple and clean. Modern looking but with a splash of this red tartan pattern.

I have another version of my logo being edited at the moment where the little top part of the F in roofing that’s currently tartan will be changed to just solid red to make it more visible. So if that’s something you can change in your mock up great. But I can provide the full version once the contest is complete

Target Market(s)

Homeowners

Industry/Entity Type

Roofing

Contact Information for Business Card

Derek Pruitt. 682-555-0193. www.copperfield roofing.co Derek@copperfieldroofing.co

Colors
EB3D1F
EC4F4E
F09395
F8D3D4
FCEDEE

Requirements
Nice to have
• Maybe instead of a business address. I could say serving all DFW Texas or something like that. And maybe add a line somewhere saying deductible assistance? Just a thought

```html
<!DOCTYPE html>
<html lang="en">
<head>
<meta charset="utf-8">
<title>Copperfield Roofing Co. — Business Card</title>
<link rel="stylesheet" href="https://fonts.googleapis.com/css2?family=Michroma&family=Open+Sans:wght@400;600&display=swap">
<style>
  :root {
    --stage: #1e1e1e;
    --card-dark: #1a1a1a;
    --card-light: #ffffff;
    --red: #d7141c;
    --ink: #1a1a1a;
    --text: #333333;
    --mark-fade: #efefef;
    --white: #ffffff;
  }
  * { margin: 0; padding: 0; box-sizing: border-box; }
  html, body {
    width: 1200px;
    height: 1122px;
    overflow: hidden;
    background: var(--stage);
  }
  .stage {
    width: 1200px;
    height: 1122px;
    display: flex;
    flex-direction: column;
    align-items: center;
    justify-content: center;
    gap: 50px;
  }
  .card {
    position: relative;
    width: 860px;
    height: 491px;
    border-radius: 26px;
    overflow: hidden;
    box-shadow: 0 12px 30px rgba(0,0,0,.45);
  }

  /* Front */
  .card--front {
    background: var(--card-dark);
    display: flex;
    flex-direction: column;
    align-items: center;
    justify-content: center;
    gap: 34px;
  }
  .brand-disc {
    width: 190px;
    height: 190px;
    border-radius: 50%;
    background: var(--red);
    border: 6px solid var(--white);
  }
  .brand-name {
    font-family: "Michroma", sans-serif;
    text-transform: uppercase;
    text-align: center;
    line-height: 1.25;
    font-size: 40px;
    color: var(--white);
    letter-spacing: 1px;
  }
  .brand-name span { display: block; }

  /* Back */
  .card--back { background: var(--card-light); }
  .faded-mark {
    position: absolute;
    left: 50px;
    top: 70px;
    width: 400px;
    height: 400px;
    border-radius: 50%;
    background: var(--mark-fade);
  }
  .back-brand {
    position: absolute;
    right: 70px;
    top: 42px;
    display: flex;
    flex-direction: column;
    align-items: center;
    gap: 18px;
  }
  .back-brand .brand-disc-small {
    width: 120px;
    height: 120px;
    border-radius: 50%;
    background: var(--red);
  }
  .back-brand .brand-name {
    font-size: 24px;
    color: var(--ink);
  }
  .rule {
    position: absolute;
    height: 4px;
    background: var(--red);
  }
  .rule--long { left: 340px; right: 40px; top: 262px; }
  .rule--short { left: 62px; width: 300px; top: 362px; }
  .holder {
    position: absolute;
    left: 62px;
    top: 280px;
  }
  .holder-name {
    font-family: "Michroma", sans-serif;
    text-transform: uppercase;
    font-size: 32px;
    color: var(--red);
    letter-spacing: 1px;
  }
  .holder-role {
    font-family: "Open Sans", sans-serif;
    font-size: 21px;
    color: var(--ink);
    margin-top: 4px;
  }
  .contact-list {
    position: absolute;
    left: 70px;
    top: 384px;
    list-style: none;
    font-family: "Open Sans", sans-serif;
    color: var(--text);
    font-size: 18px;
  }
  .contact-list li {
    display: flex;
    align-items: center;
    gap: 14px;
    height: 30px;
  }
  .contact-list .phone { font-size: 21px; }
  .contact-list svg { width: 18px; height: 18px; flex: none; }
</style>
</head>
<body>
<main class="stage">

  <section class="card card--front" aria-label="Card front">
    <div class="brand-disc"></div>
    <div class="brand-name"><span>Copperfield</span><span>Roofing Co.</span></div>
  </section>

  <section class="card card--back" aria-label="Card back">
    <div class="faded-mark" role="img" aria-label="Faint enlarged company emblem in light grey"></div>

    <div class="back-brand">
      <div class="brand-disc-small"></div>
      <div class="brand-name"><span>Copperfield</span><span>Roofing Co.</span></div>
    </div>

    <div class="rule rule--long"></div>

    <div class="holder">
      <h1 class="holder-name">Derek Pruitt</h1>
      <p class="holder-role">Founder &amp; CEO</p>
    </div>

    <div class="rule rule--short"></div>

    <ul class="contact-list">
      <li class="phone">
        <svg viewBox="0 0 24 24" aria-hidden="true"><path fill="#d7141c" d="M6.6 10.8a15 15 0 0 0 6.6 6.6l2.2-2.2c.3-.3.7-.4 1-.2 1.1.4 2.3.6 3.6.6.6 0 1 .4 1 1V20c0 .6-.4 1-1 1A17 17 0 0 1 3 4c0-.6.4-1 1-1h3.5c.6 0 1 .4 1 1 0 1.3.2 2.5.6 3.6.1.3 0 .7-.2 1z"/></svg>
        682-555-0193
      </li>
      <li>
        <svg viewBox="0 0 24 24" aria-hidden="true"><path fill="#d7141c" d="M3 5h18v14H3z"/><path fill="none" stroke="#fff" stroke-width="1.8" d="M3.5 5.5 12 13l8.5-7.5"/></svg>
        Derek@copperfieldroofing.co
      </li>
      <li>
        <svg viewBox="0 0 24 24" aria-hidden="true"><circle cx="12" cy="12" r="10" fill="#d7141c"/><path fill="none" stroke="#fff" stroke-width="1.5" d="M2 12h20M12 2c3 3 3 17 0 20M12 2c-3 3-3 17 0 20"/></svg>
        www.copperfield roofing.co
      </li>
    </ul>
  </section>

</main>
</body>
</html>
```